Business Card

I need a business card that really pops for a potential customer or person who refers a personal injury lead. I want to highlight our office locations, but only address that needs to be on the card is my office's main address. I want a sleek, modern and minimalist design.

```html
<!DOCTYPE html>
<html lang="en">
<head>
<meta charset="utf-8">
<title>Hartwell &amp; Cole – Business Card</title>
<link rel="stylesheet" href="https://fonts.googleapis.com/css2?family=Montserrat:wght@500;700&display=swap">
<style>
  :root {
    --charcoal: #3a3a3a;
    --silver: #b0b0b0;
    --paper: #ffffff;
    --ink: #2b2b2b;
    --backdrop: #e9e9ea;
  }
  * { box-sizing: border-box; margin: 0; padding: 0; }
  html, body { width: 1200px; height: 900px; overflow: hidden; }
  body {
    background: var(--backdrop);
    font-family: "Montserrat", Arial, sans-serif;
    position: relative;
  }
  .card {
    position: absolute;
    left: 250px;
    width: 700px;
    height: 400px;
    overflow: hidden;
  }
  .card--front { top: 30px; background: var(--charcoal); }
  .card--back { top: 470px; background: var(--paper); }

  .firm-name {
    position: absolute;
    font-weight: 500;
    letter-spacing: 0;
    white-space: nowrap;
    line-height: 1;
  }
  .card--front .firm-name {
    top: 50%;
    left: 50%;
    transform: translate(-50%, -50%);
    color: var(--paper);
    font-size: 46px;
  }
  .card--back .firm-name {
    left: 48px;
    top: 150px;
    color: var(--ink);
    font-size: 30px;
  }

  .wave { position: absolute; inset: 0; width: 700px; height: 400px; }
  .wave__edge { fill: var(--silver); }
  .wave__fill { fill: var(--charcoal); }

  .divider {
    position: absolute;
    left: 408px;
    top: 78px;
    width: 1.5px;
    height: 150px;
    background: var(--ink);
  }
  .contact {
    position: absolute;
    left: 428px;
    top: 60px;
    color: var(--ink);
  }
  .contact__name {
    font-weight: 700;
    font-size: 21px;
    letter-spacing: 0.01em;
  }
  .contact__title {
    font-weight: 500;
    font-size: 14px;
    margin-top: 2px;
    margin-bottom: 12px;
  }
  .contact__list { list-style: none; }
  .contact__item {
    display: flex;
    align-items: center;
    gap: 8px;
    font-size: 14px;
    font-weight: 500;
    line-height: 1.7;
  }
  .contact__icon { width: 13px; height: 13px; fill: var(--ink); flex: none; }
</style>
</head>
<body>
  <section class="card card--front" aria-label="Card front">
    <p class="firm-name">Hartwell &amp; Cole</p>
  </section>

  <section class="card card--back" aria-label="Card back">
    <svg class="wave" viewBox="0 0 700 400" aria-hidden="true">
      <path class="wave__edge" d="M206 400 C290 290 420 290 520 270 C620 250 688 160 690 40 L700 40 L700 400 Z"/>
      <path class="wave__fill" d="M222 400 C300 300 425 302 525 282 C625 262 694 170 700 58 L700 400 Z"/>
    </svg>

    <p class="firm-name">Hartwell &amp; Cole</p>

    <div class="divider"></div>

    <div class="contact">
      <p class="contact__name">DANIEL HALE</p>
      <p class="contact__title">Co-Founder</p>
      <ul class="contact__list">
        <li class="contact__item">
          <svg class="contact__icon" viewBox="0 0 24 24" aria-hidden="true"><path d="M6.6 10.8a15.1 15.1 0 0 0 6.6 6.6l2.2-2.2a1 1 0 0 1 1-.25 11.4 11.4 0 0 0 3.6.57 1 1 0 0 1 1 1V20a1 1 0 0 1-1 1A17 17 0 0 1 3 4a1 1 0 0 1 1-1h3.5a1 1 0 0 1 1 1c0 1.25.2 2.45.57 3.57a1 1 0 0 1-.25 1z"/></svg>
          555-014-2087
        </li>
        <li class="contact__item">
          <svg class="contact__icon" viewBox="0 0 24 24" aria-hidden="true"><path d="M2 5h20v14H2zm2 2v.5l8 6.3 8-6.3V7l-8 6.2z"/></svg>
          hello@hartwell-mail.com
        </li>
        <li class="contact__item">
          <svg class="contact__icon" viewBox="0 0 24 24" aria-hidden="true"><circle cx="12" cy="12" r="10"/><path d="M2 12h20M12 2c3 3 3 17 0 20M12 2c-3 3-3 17 0 20" fill="none" stroke="#fff" stroke-width="1.3"/></svg>
          www.hartwell-web.com
        </li>
      </ul>
    </div>
  </section>
</body>
</html>
```